PW Law Firm Needs Sharp Letterhead

Our law firm recently selected a new logo through Pitchgrove. Now we need a sharp Letterhead using the Letterhead.

Target Market(s)

Legal community, business clients

Industry/Entity Type

Law Firm

Requirements
Must have
• Our Logo
• Gerald P. Hollis
• Board Certified
• Civil Trial Law
• Harrow Council of Courtroom Accreditation
• ghollis@pwadvocates.net
• 2715-C West Larkin
• McAllen, TX 78504
• 956-555-0182
• www.pwadvocates.net

```html
<!DOCTYPE html>
<html lang="en">
<head>
<meta charset="utf-8">
<title>PW Law Firm Letterhead</title>
<link rel="stylesheet" href="https://fonts.googleapis.com/css2?family=EB+Garamond:ital,wght@0,400;0,500;1,400;1,600&family=Open+Sans:wght@400&display=swap">
<style>
  :root {
    --backdrop: #7f7f7f;
    --paper: #f3f4f7;
    --ink: #3a3a3c;
    --ink-soft: #5c5d62;
    --ink-muted: #8a8b90;
    --rule: #b9bbc1;
    --mark: #4a4a4d;
    --strip: #c9cbd0;
  }
  * { box-sizing: border-box; margin: 0; padding: 0; }
  html, body { width: 1200px; height: 979px; overflow: hidden; }
  body {
    background: var(--backdrop);
    display: flex;
    align-items: center;
    justify-content: center;
    font-family: "EB Garamond", Georgia, serif;
    color: var(--ink);
  }
  .letterhead {
    position: relative;
    width: 640px;
    height: 905px;
    background: var(--paper);
    box-shadow: 0 6px 20px rgba(0,0,0,0.25);
  }
  .brand {
    position: absolute;
    top: 62px;
    right: 70px;
    display: flex;
    align-items: center;
    gap: 10px;
    padding-bottom: 8px;
    border-bottom: 1px solid var(--ink-soft);
  }
  .brand-square { width: 26px; height: 26px; background: var(--mark); }
  .brand-name {
    font-size: 30px;
    font-weight: 400;
    letter-spacing: 1px;
    color: var(--mark);
  }
  .letter-date {
    position: absolute;
    top: 250px;
    right: 70px;
    text-align: right;
    font-size: 12px;
    line-height: 1.4;
    color: var(--ink-soft);
  }
  .letter-body {
    position: absolute;
    top: 170px;
    left: 70px;
    width: 400px;
    font-size: 11.5px;
    line-height: 1.45;
    color: var(--ink-soft);
  }
  .subject {
    font-style: italic;
    font-weight: 600;
    color: var(--ink);
    margin-bottom: 22px;
  }
  .salutation { font-style: italic; margin-bottom: 10px; }
  .letter-body p { margin-bottom: 10px; text-align: justify; }
  .signature-mark {
    width: 130px;
    height: 46px;
    margin: 18px 0 4px;
    background: linear-gradient(90deg, rgba(90,90,95,0.12), rgba(90,90,95,0.22), rgba(90,90,95,0.08));
  }
  .signer { font-size: 12px; line-height: 1.4; color: var(--ink-soft); }
  .signer-name { color: var(--ink); font-weight: 500; }
  .letter-footer {
    position: absolute;
    left: 70px;
    right: 70px;
    bottom: 54px;
    display: flex;
    font-family: "Open Sans", Arial, sans-serif;
    font-size: 9px;
    line-height: 1.55;
    color: var(--ink-muted);
  }
  .footer-col { padding: 0 14px; border-left: 1px solid var(--rule); min-height: 48px; }
  .footer-col:first-child { padding-left: 0; border-left: none; width: 150px; }
  .footer-col.contact { width: 164px; }
  .footer-col.web { flex: 1; }
  .footer-strip {
    position: absolute;
    left: 384px;
    bottom: 0;
    width: 186px;
    height: 14px;
    background: var(--strip);
  }
</style>
</head>
<body>
  <main class="letterhead">
    <header class="brand">
      <span class="brand-square"></span>
      <span class="brand-name">PW Law Firm</span>
    </header>

    <div class="letter-date">18.11.2013<br>McAllen</div>

    <section class="letter-body">
      <div class="subject">Semper sed feugiat felis hendrerit<br>ACCD Aenean scelerisque lorem aliquam.</div>
      <div class="salutation">Vitae gravida,</div>
      <p>Lorem ipsum dolor sit amet, consectetur adipiscing elit. Aenean aliquet, dui sodales blandit accumsan, lorem arcu volutpat orci, eu ultricies nisl mi id turpis. Integer non vulputate magna. Fusce nisl leo, pharetra non fringilla in, ultricies sed ante.</p>
      <p>Pellentesque gravida porttitor dolor sed convallis. Morbi vehicula venenatis consectetur. Cras et mauris metus. Lorem ipsum dolor sit amet, consectetur adipiscing elit. Fusce porta dui sed leo posuere.</p>
      <p>Donec sed odio sit amet nisl fermentum rhoncus. Integer eget nulla egestas laoreet, illa purus mollis metus, vel sagittis nunc augue nec odio. Ut convallis malesuada mauris eu pellentesque.</p>
      <p>Etiam placerat magna accumsan, arcu dolor accumsan turpis, vitae gravida ipsum nisi non lorem. Aenean egestas commodo blandit. Nullam ut quam lacus. Curabitur mollis tortor non lectus dapibus vulputate. Vivamus commodo diam non.</p>
      <div class="signature-mark" role="img" aria-label="Handwritten signature"></div>
      <div class="signer">
        <span class="signer-name">Gerald P. Hollis</span><br>
        Board Certified &ndash; Civil Trial Law<br>
        Harrow Council of Courtroom Accreditation
      </div>
    </section>

    <footer class="letter-footer">
      <div class="footer-col address">2715-C West Larkin<br>McAllen, TX 78504</div>
      <div class="footer-col contact">T: 956-555-0182<br>E: ghollis@pwadvocates.net</div>
      <div class="footer-col web">www.pwadvocates.net</div>
    </footer>
    <div class="footer-strip"></div>
  </main>
</body>
</html>
```